tavremsupply.com

I had a logo designed by pixel forge, and now need a website. I would like all the normal features a website would need.
Payment method etc and I'd like to be able to upload pictures

Target Market(s)

Parents, gift ideas, baby shower, online shopping

Industry/Entity Type

Crowd

Coding

Coded - Design and coding required

Number of Pages Required

1 page

Requirements
Must have
• Would like it to be accessible using a mobile phone
• must be given DNS code so i can add pages as needed
• must be able to upload pictures of products, and up date as needed
Nice to have
• additional pages with no content

```html
<!DOCTYPE html>
<html lang="en">
<head>
<meta charset="utf-8">
<title>Tavrem – Baby Store</title>
<link rel="stylesheet" href="https://fonts.googleapis.com/css2?family=Ubuntu:wght@400;500;700&family=Open+Sans:wght@400;600;700&display=swap">
<style>
:root{
  --orange:#f0a010;
  --red:#e8194c;
  --blue:#3ca4f0;
  --pink:#ee4a6c;
  --green:#8cc63f;
  --yellow:#f6c61c;
  --text:#444;
  --muted:#999;
  --price:#3ca4f0;
  --bg:#fbfbfb;
  --line:#e3e3e3;
}
*{margin:0;padding:0;box-sizing:border-box}
html,body{width:1200px;height:1200px;overflow:hidden;background:#fff}
body{font-family:"Open Sans",sans-serif;color:var(--text);position:relative}
.page{position:absolute;left:392px;top:0;width:530px;height:1500px;background:var(--bg);transform:scale(.8);transform-origin:0 0;overflow:hidden}
.abs{position:absolute}
.topbar{top:0;left:0;width:530px;height:18px;background:#fff;font-size:5.5px;color:var(--muted)}
.topbar span{position:absolute;top:6px}
.header{top:18px;left:0;width:530px;height:37px;background:var(--orange)}
.wave{position:absolute;left:0;width:530px;height:6px;background:radial-gradient(circle at 5px 6px,var(--orange) 4.6px,transparent 5px) 0 0/10px 6px repeat-x}
.logo{left:38px;top:9px;font-family:Ubuntu,sans-serif;font-size:18px;color:#fff;font-weight:400}
.nav a{position:absolute;top:17px;font-size:5.5px;font-weight:700;color:#fff;text-decoration:none;font-family:Ubuntu,sans-serif}
.cart{left:468px;top:10px;width:24px;height:24px;border-radius:50%;background:var(--pink);color:#fff;font-size:6px;text-align:center;line-height:24px}
.redband{top:55px;left:0;width:530px;height:23px;background:var(--red)}
.search{left:155px;top:60px;width:340px;height:15px;border-radius:8px;background:#fff;font-size:5px;color:#bbb;padding:4px 10px}
.search i{position:absolute;right:2px;top:2px;width:11px;height:11px;border-radius:50%;background:var(--green)}
.cats{left:37px;top:55px;width:105px;height:224px;background:var(--blue)}
.cats h3{background:#2f8fe0;color:#fff;font-family:Ubuntu,sans-serif;font-weight:500;font-size:9px;padding:6px 7px;height:22px}
.cats li{list-style:none;color:#fff;font-size:5px;font-weight:600;height:22.3px;line-height:22px;padding-left:7px;border-bottom:1px solid rgba(255,255,255,.2)}
.hero{left:142px;top:78px;width:247px;height:201px;background:linear-gradient(120deg,#d8d8d8,#eeeae6 55%,#cfcfcf)}
.hero b{position:absolute;left:4px;top:30px;font-family:Ubuntu,sans-serif;font-weight:400;font-size:32px;color:#333}
.tile{width:105px;color:#fff;text-align:center;font-family:Ubuntu,sans-serif}
.tile strong{display:block;font-size:24px;font-weight:700;margin-top:28px}
.tile small{font-size:8px;letter-spacing:.5px}
.step{top:292px;height:32px;color:#fff;font-family:Ubuntu,sans-serif;font-size:14px;text-align:center;line-height:32px;letter-spacing:.5px}
.dot{top:298px;width:20px;height:20px;border-radius:50%;background:var(--yellow);border:2px solid #f3d98a}
.h2{font-family:Ubuntu,sans-serif;font-size:12px;font-weight:400}
.h2 em{font-style:normal}
.arrow{top:349px;width:14px;height:14px;border-radius:50%;border:1px solid var(--pink);color:var(--pink);font-size:8px;text-align:center;line-height:12px}
.img{border-radius:6px}
.card{text-align:center;width:90px}
.card .t{font-size:8px;color:#333}
.card .p{font-size:8px;color:var(--price);margin-top:3px}
.btn{display:inline-block;border:1px solid var(--line);font-size:4.6px;font-weight:700;color:#888;width:64px;height:16px;line-height:14px;margin-top:5px;background:#fff}
.banner{top:688px;height:83px}
.pill{background:#fff;border-radius:8px;font-size:4.6px;font-weight:700;color:#555;text-align:center;line-height:14px;height:14px}
.sec{top:788px;font-family:Ubuntu,sans-serif;font-weight:500;font-size:10.5px;color:var(--blue)}
.deal{left:38px;top:810px;width:97px;height:190px;background:#fff}
.cd{top:972px;width:19px;height:16px;background:#e9f2fb;font-size:5px;text-align:center;font-weight:700;color:#555;line-height:8px;padding-top:1px}
.cd small{display:block;font-size:3.5px;color:#999;font-weight:400;line-height:5px}
.na{text-align:center;width:70px}
.na .t{font-size:7px;color:#333}
.na .p{font-size:6.5px;color:var(--price)}
.na .btn{width:62px}
.viewall{left:164px;top:1047px;width:206px;height:16px;background:#e3effa;font-size:5px;color:#6a8fb5;text-align:center;line-height:16px}
.seller{left:385px;width:109px;height:44px;border-bottom:1px solid var(--line);background:#fff}
.seller .th{position:absolute;left:5px;top:12px;width:20px;height:16px;background:linear-gradient(#cfe3f5,#f5c9d2);border-radius:3px}
.seller .t{position:absolute;left:34px;top:8px;font-size:6.5px;color:#333}
.seller .p{position:absolute;left:48px;top:20px;font-size:6.5px;color:var(--price)}
.promo{top:1120px;width:144px;height:93px}
.promo .k{position:absolute;left:14px;top:30px;font-family:Ubuntu,sans-serif;font-size:7px;font-weight:700;color:rgba(255,255,255,.8)}
.promo .n{position:absolute;left:14px;top:40px;font-family:Ubuntu,sans-serif;font-size:15px;font-weight:700;color:#fff}
.promo .d{position:absolute;left:14px;top:68px;width:62px;height:14px;border:1px solid #fff;border-radius:8px;font-size:4.6px;color:#fff;text-align:center;line-height:12px}
.brand{top:1244px;font-family:Ubuntu,sans-serif;font-size:9px;letter-spacing:1.5px;color:#aaa}
.news{left:37px;top:1271px;width:457px;height:51px;border:1px solid var(--line);background:#fff}
.soc{top:1289px;width:15px;height:15px;border-radius:50%;border:1px solid #ccc;background:#fff}
.soc::after{content:"";position:absolute;left:5px;top:5px;width:4px;height:4px;border-radius:50%}
.footer{left:0;top:1351px;width:530px;height:127px;background:var(--orange);color:#fff}
.footer h4{position:absolute;top:22px;font-family:Ubuntu,sans-serif;font-weight:400;font-size:10px}
.footer p{position:absolute;font-size:5px;line-height:14px}
.up{left:468px;top:1335px;width:24px;height:24px;border-radius:50%;background:var(--blue);color:#fff;text-align:center;line-height:22px;font-size:10px}
.copy{left:0;top:1478px;width:530px;height:22px;background:var(--red);color:#fff;font-size:5px;text-align:center;line-height:22px}
</style>
</head>
<body>
<div class="page">

  <div class="abs topbar">
    <span style="left:38px">&#9679; Find location</span>
    <span style="left:92px">&#9990; 0140-552-318</span>
    <span style="left:320px">USD &#9662;</span>
    <span style="left:362px">English &#9662;</span>
    <span style="left:412px">My account &#9662;</span>
  </div>

  <header class="abs header">
    <div class="wave" style="top:-5px"></div>
    <div class="abs logo">Tavrem</div>
    <nav class="nav">
      <a style="left:155px">HOME</a><a style="left:196px">SHOP</a><a style="left:232px">COLLECTION</a><a style="left:292px">NEW</a><a style="left:334px">CONTACT</a>
    </nav>
  </header>
  <div class="abs cart">&#9632; 0</div>

  <div class="abs redband"></div>
  <div class="abs search">Search our catalog<i></i></div>

  <aside class="abs cats">
    <h3>Categories</h3>
    <ul>
      <li>Clothings</li><li>Healthy food</li><li>Toys</li><li>Book</li><li>Shower Gel</li><li>Milk</li><li>Accessories</li><li>Schools</li><li style="border:0">Other Categories</li>
    </ul>
  </aside>

  <div class="abs hero" role="img" aria-label="Baby in a white shirt beside the store name"><b>Tavrem</b></div>
  <div class="abs tile" style="left:389px;top:78px;height:103px;background:linear-gradient(#f3b744,#e9a21c)" role="img" aria-label="Gift basket photo with Gifts caption"><strong>Gifts</strong><small>BABY GIFTS</small></div>
  <div class="abs tile" style="left:389px;top:181px;height:98px;background:linear-gradient(#e8506c,#d33556)" role="img" aria-label="Baby shower photo with Shower caption"><strong style="margin-top:26px">Shower</strong><small>BABY SHOWER</small></div>

  <div class="abs step" style="left:37px;width:110px;background:var(--orange)">PURCHASE</div>
  <div class="abs dot" style="left:155px"></div>
  <div class="abs step" style="left:194px;width:111px;background:var(--blue)">SHIPPING</div>
  <div class="abs dot" style="left:312px"></div>
  <div class="abs step" style="left:350px;width:112px;background:var(--pink)">DELIVERD</div>
  <div class="abs dot" style="left:468px"></div>

  <h2 class="abs h2" style="left:36px;top:347px"><em style="color:var(--pink)">Our Best</em> <em style="color:var(--blue)">Products</em></h2>
  <div class="abs arrow" style="left:456px">&larr;</div>
  <div class="abs arrow" style="left:476px">&rarr;</div>

  <div class="abs img" style="left:55px;top:405px;width:125px;height:140px;background:linear-gradient(#8fd4e8,#9c8fd6)" role="img" aria-label="Plush toy gift basket"></div>
  <div class="abs card" style="left:80px;top:558px"><div class="t">BabyProducts 1</div><div class="p">$25.50</div><span class="btn">ADD TO CART</span></div>

  <div class="abs img" style="left:228px;top:390px;width:70px;height:72px;background:linear-gradient(#c9dff2,#9fb7cf)" role="img" aria-label="Gift basket"></div>
  <div class="abs img" style="left:323px;top:390px;width:70px;height:72px;background:linear-gradient(#d8eef3,#8ccbd8)" role="img" aria-label="Baby bouncer"></div>
  <div class="abs img" style="left:413px;top:385px;width:70px;height:80px;background:linear-gradient(#fff6c2,#f0d64a)" role="img" aria-label="Bath set basket"></div>
  <div class="abs card" style="left:218px;top:468px"><div class="t">BabyProducts 1</div><div class="p">$25.50</div><span class="btn">ADD TO CART</span></div>
  <div class="abs card" style="left:313px;top:468px"><div class="t">BabyProducts 1</div><div class="p">$25.50</div><span class="btn">ADD TO CART</span></div>
  <div class="abs card" style="left:403px;top:468px"><div class="t">BabyProducts 1</div><div class="p">$25.50</div><span class="btn">ADD TO CART</span></div>

  <div class="abs img" style="left:228px;top:528px;width:70px;height:72px;background:linear-gradient(#c8e6ef,#f1c8d4)" role="img" aria-label="Plush animal set"></div>
  <div class="abs img" style="left:330px;top:520px;width:56px;height:80px;background:linear-gradient(#f2f2f2,#cfd4d8)" role="img" aria-label="Baby monitor"></div>
  <div class="abs img" style="left:413px;top:520px;width:70px;height:80px;background:linear-gradient(#b8d4ec,#8fb2d6)" role="img" aria-label="Teddy bear nappy cake"></div>
  <div class="abs card" style="left:218px;top:610px"><div class="t">BabyProducts 1</div><div class="p">$25.50</div><span class="btn">ADD TO CART</span></div>
  <div class="abs card" style="left:313px;top:610px"><div class="t">BabyProducts 1</div><div class="p">$25.50</div><span class="btn">ADD TO CART</span></div>
  <div class="abs card" style="left:403px;top:610px"><div class="t">BabyProducts 1</div><div class="p">$25.50</div><span class="btn">ADD TO CART</span></div>

  <div class="abs banner" style="left:37px;width:228px;background:linear-gradient(90deg,#d6e2ee,#c7d6e6)" role="img" aria-label="Child in white shirt">
    <div class="abs" style="left:26px;top:14px;font-family:Ubuntu,sans-serif;font-size:14px;color:#8aa0b6">Just for kid</div>
    <div class="abs" style="left:40px;top:32px;font-size:4.6px;color:#8aa0b6">SPECIALLY BABY</div>
    <div class="abs pill" style="left:30px;top:49px;width:68px">VIEW COLLECTION</div>
  </div>
  <div class="abs banner" style="left:265px;width:229px;background:linear-gradient(90deg,#f05a6a,#e53a55)" role="img" aria-label="Toddler in graduation cap with abacus">
    <div class="abs" style="left:140px;top:4px;font-family:Ubuntu,sans-serif;font-weight:700;font-size:25px;color:#fff">Back</div>
    <div class="abs" style="left:140px;top:34px;font-family:Ubuntu,sans-serif;font-weight:700;font-size:14px;color:#fff">to school</div>
    <div class="abs" style="left:155px;top:57px;font-size:4.8px;color:#fff;border-bottom:1px solid #fff;padding-bottom:2px">DISCOVER MORE &rarr;</div>
  </div>

  <h3 class="abs sec" style="left:38px">Today Deals</h3>
  <h3 class="abs sec" style="left:156px">New Arrivals</h3>
  <h3 class="abs sec" style="left:389px">Best Sellerrs</h3>

  <div class="abs deal"></div>
  <div class="abs img" style="left:55px;top:830px;width:65px;height:77px;background:linear-gradient(#dcf0f5,#8ccbd8)" role="img" aria-label="Baby bouncer"></div>
  <div class="abs" style="left:38px;top:919px;width:97px;text-align:center">
    <div style="font-size:8px;color:#333">BabyProducts 1</div>
    <div style="font-size:8px;color:var(--price);margin-top:6px">$25.50</div>
    <div style="font-size:7px;color:#333;margin-top:4px">Our previous price <span style="color:var(--pink)">$35</span></div>
  </div>
  <div class="abs cd" style="left:45px">464<small>DAYS</small></div>
  <div class="abs cd" style="left:68px">08<small>HOURS</small></div>
  <div class="abs cd" style="left:92px">33<small>MIN</small></div>
  <div class="abs cd" style="left:115px">27<small>SEC</small></div>

  <div class="abs img" style="left:176px;top:828px;width:40px;height:45px;background:linear-gradient(#cfe8fa,#3c93d8)" role="img" aria-label="Baby bottle"></div>
  <div class="abs img" style="left:244px;top:826px;width:46px;height:48px;background:linear-gradient(#fbe59a,#f3a6b8)" role="img" aria-label="Baby care bottles"></div>
  <div class="abs img" style="left:320px;top:823px;width:34px;height:55px;background:linear-gradient(#fff6c2,#f0d64a)" role="img" aria-label="Bath set basket"></div>
  <div class="abs na" style="left:161px;top:880px"><div class="t">BabyProducts 2</div><div class="p">$25.50</div><span class="btn">ADD TO CART</span></div>
  <div class="abs na" style="left:232px;top:880px"><div class="t">BabyProducts 2</div><div class="p">$25.50</div><span class="btn">ADD TO CART</span></div>
  <div class="abs na" style="left:302px;top:880px"><div class="t">BabyProducts 2</div><div class="p">$25.50</div><span class="btn">ADD TO CART</span></div>

  <div class="abs img" style="left:176px;top:937px;width:40px;height:45px;background:linear-gradient(#cfe8fa,#3c93d8)" role="img" aria-label="Baby bottle"></div>
  <div class="abs img" style="left:244px;top:935px;width:46px;height:48px;background:linear-gradient(#fbe59a,#f3a6b8)" role="img" aria-label="Baby care bottles"></div>
  <div class="abs img" style="left:320px;top:932px;width:34px;height:55px;background:linear-gradient(#fff6c2,#f0d64a)" role="img" aria-label="Bath set basket"></div>
  <div class="abs na" style="left:161px;top:989px"><div class="t">BabyProducts 2</div><div class="p">$25.50</div><span class="btn">ADD TO CART</span></div>
  <div class="abs na" style="left:232px;top:989px"><div class="t">BabyProducts 2</div><div class="p">$25.50</div><span class="btn">ADD TO CART</span></div>
  <div class="abs na" style="left:302px;top:989px"><div class="t">BabyProducts 2</div><div class="p">$25.50</div><span class="btn">ADD TO CART</span></div>
  <div class="abs viewall">VIEW ALL ITEMS</div>

  <div class="abs seller" style="top:812px"><span class="th" role="img" aria-label="Product thumbnail"></span><span class="t">BabyProducts 2</span><span class="p">$25.50</span></div>
  <div class="abs seller" style="top:857px"><span class="th" role="img" aria-label="Product thumbnail"></span><span class="t">BabyProducts 2</span><span class="p">$25.50</span></div>
  <div class="abs seller" style="top:900px"><span class="th" role="img" aria-label="Product thumbnail"></span><span class="t">BabyProducts 2</span><span class="p">$25.50</span></div>
  <div class="abs seller" style="top:947px"><span class="th" role="img" aria-label="Product thumbnail"></span><span class="t">BabyProducts 2</span><span class="p">$25.50</span></div>
  <div class="abs seller" style="top:993px"><span class="th" role="img" aria-label="Product thumbnail"></span><span class="t">BabyProducts 2</span><span class="p">$25.50</span></div>
  <div class="abs seller" style="top:1041px"><span class="th" role="img" aria-label="Product thumbnail"></span><span class="t">BabyProducts 2</span><span class="p">$25.50</span></div>

  <div class="abs promo" style="left:37px;background:linear-gradient(90deg,#8cc63f,#9fd14f)" role="img" aria-label="Toy dinosaur on wheels">
    <span class="k">New Arrivals</span><span class="n">Dinosaur</span><span class="d">DISCOVER NOW</span>
  </div>
  <div class="abs promo" style="left:193px;background:radial-gradient(circle at 50% 50%,#ff3b2f 0 28%,#ef4b5a 30%)" role="img" aria-label="Red toy crab"></div>
  <div class="abs promo" style="left:349px;background:linear-gradient(90deg,#f4c21a,#f8d445)" role="img" aria-label="Yellow rubber duck">
    <span class="k">New Arrivals</span><span class="n">Cute Dark</span><span class="d">DISCOVER NOW</span>
  </div>

  <div class="abs brand" style="left:49px">NORVA</div>
  <div class="abs brand" style="left:126px">KESTLE</div>
  <div class="abs brand" style="left:204px">BAGLO</div>
  <div class="abs brand" style="left:280px">BYRDEN</div>
  <div class="abs brand" style="left:357px">MILOVA</div>
  <div class="abs brand" style="left:434px">WENSHOP</div>

  <div class="abs news"></div>
  <div class="abs" style="left:55px;top:1289px;font-family:Ubuntu,sans-serif;font-size:11px;color:var(--blue)">Newsletter</div>
  <div class="abs" style="left:148px;top:1288px;width:184px;height:16px;border-radius:8px;background:#e6eff7;font-size:4.6px;color:#aab;padding:5px 6px">Your email address<span style="position:absolute;right:8px;top:5px;width:6px;height:5px;background:var(--green)"></span></div>
  <div class="abs soc" style="left:393px"></div>
  <div class="abs soc" style="left:414px"></div>
  <div class="abs soc" style="left:436px"></div>
  <div class="abs soc" style="left:458px"></div>

  <footer class="abs footer">
    <div class="wave" style="top:-5px"></div>
    <h4 style="left:37px">Support</h4>
    <p style="left:37px;top:46px">Shipping &amp; Returns<br>Policy<br>Terms &amp; Condition<br>Guarantee</p>
    <h4 style="left:116px">Account</h4>
    <p style="left:116px;top:45px">Address<br>Payment Slip<br>Orders<br>Personal Info</p>
    <h4 style="left:194px">Popular Tags</h4>
    <p style="left:194px;top:45px">Babby Clothes&nbsp;&nbsp;&nbsp; Gifts&nbsp;&nbsp;&nbsp; New Arrivals<br>Shoes&nbsp;&nbsp;&nbsp;&nbsp;&nbsp;&nbsp;&nbsp;&nbsp;&nbsp;&nbsp;&nbsp;&nbsp;&nbsp;&nbsp;&nbsp; Shop&nbsp;&nbsp; Jackets</p>
    <h4 style="left:350px">Keep In Touch</h4>
    <p style="left:350px;top:45px;line-height:8px">12 Orchard Lane, Brookfield<br>Park<br><br>0140-552-318 , 0140-552-319<br><br>hello@tavremsupply.com</p>
  </footer>
  <div class="abs up">&uarr;</div>
  <div class="abs copy">© Copyright 2017 By Tavrem</div>

</div>
</body>
</html>
```